Telecom company needs marketing flyers

We need 3 different flyers to describe our product and how to qualify for the program. This our website to use for the logo and color scheme https://www.brivolinkmobile.com, however do not use the mascot on the flyer.

Attached are examples of a competitors flyers.

```html
<!DOCTYPE html>
<html lang="en">
<head>
<meta charset="utf-8">
<title>Brivolink Mobile – Flyers</title>
<link rel="stylesheet" href="https://fonts.googleapis.com/css2?family=Plus+Jakarta+Sans:ital,wght@0,300;0,400;0,500;0,600;0,700;0,800;1,500;1,700&display=swap">
<style>
:root{
  --blue:#1d97d8;
  --teal:#2bbfa6;
  --ink:#141414;
  --muted:#5b6b78;
  --page:#ebe8e5;
  --white:#ffffff;
  --brand-gradient:linear-gradient(90deg,var(--blue) 0%,var(--teal) 100%);
}
*{box-sizing:border-box;margin:0;padding:0}
html,body{width:1200px;height:5073px;overflow:hidden}
body{background:var(--page);font-family:"Plus Jakarta Sans",Arial,sans-serif;color:var(--ink);position:relative}
.flyer{position:absolute;left:49px;width:1102px;height:1560px;background:var(--white);box-shadow:0 10px 24px rgba(0,0,0,.16);overflow:hidden}
.flyer--coverage{top:85px}
.flyer--tablet{top:1728px}
.flyer--eligibility{top:3350px}
.brand{position:absolute;left:108px;top:118px;color:var(--blue);font-weight:400;line-height:1}
.brand__name{display:block;font-size:40px;letter-spacing:9px}
.brand__sub{display:block;font-size:14px;letter-spacing:4px;text-align:right;margin-top:6px;padding-right:4px}
.footer-bar{position:absolute;left:0;bottom:0;width:100%;height:47px;background:var(--brand-gradient);color:var(--white);font-weight:700;font-size:19px;display:flex;align-items:center;justify-content:center}
.fine-print{position:absolute;left:108px;width:890px;font-size:10.5px;line-height:14.5px;color:#333;text-align:justify}
.steps{position:absolute;left:108px}
.steps__title{font-size:30px;font-weight:700;margin-bottom:22px}
.steps__list{list-style:none}
.steps__item{display:flex;align-items:center;font-size:29px;font-weight:400;min-height:57px;line-height:1.15}
.steps__icon{width:46px;height:46px;margin-right:20px;flex:none}
.call{position:absolute;left:108px;display:flex;align-items:center}
.call__icon{width:110px;height:110px;margin-right:26px}
.call__tag{font-size:23px;font-style:italic;font-weight:700;color:var(--teal)}
.call__line{font-size:39px;font-weight:400;line-height:1.1}
.call__line b{font-weight:800}

/* Flyer 1 */
.hero-photo{position:absolute;left:660px;top:217px;width:442px;height:1052px;background:linear-gradient(160deg,#cfe3e6 0%,#b8cfd2 40%,#7d8f96 75%,#4b5a63 100%)}
.price-badge{position:absolute;left:770px;top:0;width:276px;height:435px;background:linear-gradient(135deg,var(--blue) 0%,var(--teal) 100%);color:var(--white);padding:148px 0 0 32px}
.price-badge__lead{font-size:36px;font-weight:700;line-height:.98}
.price-badge__for{display:flex;align-items:flex-end;font-size:36px;font-weight:700;margin-top:6px}
.price-badge__amount{font-size:118px;font-weight:800;line-height:.8;margin-left:30px;letter-spacing:-2px}
.price-badge__note{font-size:23px;font-weight:600;margin-top:34px}
.headline{position:absolute;left:112px;top:300px;font-size:64px;line-height:72px;letter-spacing:-.5px}
.headline__strong{display:block;font-weight:800}
.headline__light{display:block;font-weight:300;color:var(--blue)}

/* Flyer 2 */
.ribbon-label{position:absolute;left:467px;top:89px;width:635px;height:95px;background:var(--brand-gradient);color:var(--white);font-size:45px;font-weight:700;letter-spacing:3px;display:flex;align-items:center;padding-left:60px}
.gift-tablet{position:absolute;left:560px;top:285px;width:542px;height:1228px;background:linear-gradient(180deg,#c9c8ee 0%,#e8d7ea 40%,#f4e3d3 65%,#f6f2ee 100%);z-index:0}
.big-headline{position:absolute;left:112px;top:352px;font-size:86px;font-weight:800;line-height:93px;letter-spacing:-1px;z-index:1}
.accent-rule{position:absolute;left:108px;height:10px;background:var(--brand-gradient)}
.flyer--tablet .steps,.flyer--tablet .call,.flyer--tablet .fine-print{z-index:1}

/* Flyer 3 */
.section-band{position:absolute;left:0;top:223px;width:100%;height:79px;background:var(--brand-gradient);color:var(--white);font-size:35px;font-weight:700;letter-spacing:3px;display:flex;align-items:center;padding-left:108px}
.section-title{position:absolute;left:112px;top:372px;font-size:66px;font-weight:800;letter-spacing:-.5px}
.intro{position:absolute;left:108px;top:516px;width:890px;font-size:27.5px;font-weight:700;line-height:35px}
.programs{position:absolute;left:108px;top:648px;list-style:none;font-size:19px;color:var(--muted);line-height:29.6px}
.programs li{padding-left:20px;position:relative}
.programs li::before{content:"";position:absolute;left:2px;top:12px;width:7px;height:7px;border-radius:50%;background:var(--blue)}
.programs b{font-weight:700;color:#3b4a56}
.qualify-box{position:absolute;left:53px;top:1211px;width:991px;height:171px;border:3px solid var(--teal);border-left-color:var(--blue);display:flex;align-items:center}
.qualify-box__text{width:497px;padding-left:52px;font-size:22.5px;font-style:italic;font-weight:500;line-height:29px}
.qualify-box__text b{font-weight:700}
.qualify-box__divider{width:2px;height:120px;background:#cfd6db}
.qualify-box__call{display:flex;align-items:center;padding-left:38px}
.qualify-box__icon{width:76px;height:76px;margin-right:18px}
.qualify-box__line{font-size:38px;line-height:1.15}
.qualify-box__line b{font-weight:800}
</style>
</head>
<body>

<!-- Flyer 1: free service with tablet -->
<section class="flyer flyer--coverage">
  <div class="brand"><span class="brand__name">BRIVOLINK</span><span class="brand__sub">MOBILE</span></div>
  <div class="hero-photo" role="img" aria-label="Photo of a smiling family on a sofa looking at a tablet together"></div>
  <div class="price-badge">
    <p class="price-badge__lead">Nationwide<br>coverage</p>
    <p class="price-badge__for">for <span class="price-badge__amount">$0</span></p>
    <p class="price-badge__note">Limited time only!</p>
  </div>
  <h1 class="headline">
    <span class="headline__strong">Free Service<br>&amp; Internet with<br>Your Tablet!</span>
    <span class="headline__light">Get Your<br>Limited Time<br>Deal Today!</span>
  </h1>
  <div class="steps" style="top:872px">
    <p class="steps__title">Follow these simple steps:</p>
    <ul class="steps__list">
      <li class="steps__item"><svg class="steps__icon" viewBox="0 0 48 48" fill="none" stroke="#1d97d8" stroke-width="2.5"><path d="M24 44s14-14 14-25a14 14 0 0 0-28 0c0 11 14 25 14 25z"/><circle cx="24" cy="19" r="5"/></svg>Check coverage in your area</li>
      <li class="steps__item"><svg class="steps__icon" viewBox="0 0 48 48" fill="none" stroke="#1d97d8" stroke-width="2.5"><path d="M8 42l3-9a18 18 0 1 1 6 6z"/><path d="M18 15l3 0 2 5-2 2a11 11 0 0 0 5 5l2-2 5 2v3c-7 1-16-8-15-15z"/></svg>Get in touch with us</li>
      <li class="steps__item"><svg class="steps__icon" viewBox="0 0 48 48" fill="none" stroke="#1d97d8" stroke-width="2.5" stroke-linejoin="round"><path d="M14 44V26l-5-7 3-2 6 6V8a3 3 0 0 1 6 0v12 -3a3 3 0 0 1 6 0v4a3 3 0 0 1 6 0v14c0 6-3 9-6 11"/><path d="M30 6l4-4M34 10l5-2"/></svg>Pick Your Plan</li>
      <li class="steps__item" style="align-items:flex-start"><svg class="steps__icon" viewBox="0 0 48 48" fill="none" stroke="#1d97d8" stroke-width="2.5"><path d="M3 6h7l6 26h24l4-18H12"/><circle cx="19" cy="40" r="3"/><circle cx="36" cy="40" r="3"/></svg>Place Order, Active Your Plan,<br>and Enjoy!</li>
    </ul>
  </div>
  <div class="call" style="top:1282px">
    <svg class="call__icon" viewBox="0 0 110 110" fill="none" stroke-width="6" stroke-linecap="round"><path stroke="#1d97d8" d="M22 10l16 0 8 22-10 9c6 14 17 25 31 31l9-10 22 8v16c-40 6-82-36-76-76z"/><path stroke="#2bbfa6" d="M62 22a26 26 0 0 1 26 26M62 6a42 42 0 0 1 42 42"/></svg>
    <div>
      <p class="call__tag">Fast, Easy &amp; Free Service!</p>
      <p class="call__line">Call Now <b>+800-555-0142</b></p>
    </div>
  </div>
  <p class="fine-print" style="top:1416px">Service is available to eligible customers only and is limited to one account per household. Plan features, coverage and device models may vary by location and stock. Proof of enrollment in a qualifying program is required at sign up. Offers may change or end without notice. Taxes and fees may apply where required by law. Devices are subject to availability and cannot be exchanged for cash. See full terms online before you order.</p>
  <div class="footer-bar">www.brivolinkmobile.com</div>
</section>

<!-- Flyer 2: free tablet -->
<section class="flyer flyer--tablet">
  <div class="brand"><span class="brand__name">BRIVOLINK</span><span class="brand__sub">MOBILE</span></div>
  <div class="ribbon-label">LIMITED TIME ONLY !</div>
  <div class="gift-tablet" role="img" aria-label="Hand holding up a tablet wrapped with a red gift ribbon and bow"></div>
  <h1 class="big-headline">Get your<br>next new<br>tablet<br>for free</h1>
  <div class="accent-rule" style="top:755px;width:311px"></div>
  <div class="steps" style="top:918px">
    <p class="steps__title">Follow these simple steps:</p>
    <ul class="steps__list">
      <li class="steps__item"><svg class="steps__icon" viewBox="0 0 48 48" fill="none" stroke="#1d97d8" stroke-width="2.5"><path d="M24 44s14-14 14-25a14 14 0 0 0-28 0c0 11 14 25 14 25z"/><circle cx="24" cy="19" r="5"/></svg>Check coverage in your area</li>
      <li class="steps__item"><svg class="steps__icon" viewBox="0 0 48 48" fill="none" stroke="#1d97d8" stroke-width="2.5"><path d="M8 42l3-9a18 18 0 1 1 6 6z"/><path d="M18 15l3 0 2 5-2 2a11 11 0 0 0 5 5l2-2 5 2v3c-7 1-16-8-15-15z"/></svg>Get in touch with us</li>
      <li class="steps__item"><svg class="steps__icon" viewBox="0 0 48 48" fill="none" stroke="#1d97d8" stroke-width="2.5" stroke-linejoin="round"><path d="M14 44V26l-5-7 3-2 6 6V8a3 3 0 0 1 6 0v12 -3a3 3 0 0 1 6 0v4a3 3 0 0 1 6 0v14c0 6-3 9-6 11"/><path d="M30 6l4-4M34 10l5-2"/></svg>Pick Your Plan</li>
      <li class="steps__item"><svg class="steps__icon" viewBox="0 0 48 48" fill="none" stroke="#1d97d8" stroke-width="2.5"><path d="M3 6h7l6 26h24l4-18H12"/><circle cx="19" cy="40" r="3"/><circle cx="36" cy="40" r="3"/></svg>Place Order, Active Your Plan, and Enjoy!</li>
    </ul>
  </div>
  <div class="call" style="top:1280px">
    <svg class="call__icon" viewBox="0 0 110 110" fill="none" stroke-width="6" stroke-linecap="round"><path stroke="#1d97d8" d="M22 10l16 0 8 22-10 9c6 14 17 25 31 31l9-10 22 8v16c-40 6-82-36-76-76z"/><path stroke="#2bbfa6" d="M62 22a26 26 0 0 1 26 26M62 6a42 42 0 0 1 42 42"/></svg>
    <div>
      <p class="call__tag">Fast, Easy &amp; Free Service!</p>
      <p class="call__line">Call Now <b>+800-555-0142</b></p>
    </div>
  </div>
  <p class="fine-print" style="top:1414px">Service is available to eligible customers only and is limited to one account per household. Plan features, coverage and device models may vary by location and stock. Proof of enrollment in a qualifying program is required at sign up. Offers may change or end without notice. Taxes and fees may apply where required by law. Devices are subject to availability and cannot be exchanged for cash. See full terms online before you order.</p>
  <div class="footer-bar">www.brivolinkmobile.com</div>
</section>

<!-- Flyer 3: eligibility -->
<section class="flyer flyer--eligibility">
  <div class="brand"><span class="brand__name">BRIVOLINK</span><span class="brand__sub">MOBILE</span></div>
  <div class="section-band">PROGRAM-BASED ELIGIBILITY</div>
  <h1 class="section-title">How to Qualify</h1>
  <div class="accent-rule" style="top:462px;width:217px;height:9px"></div>
  <p class="intro">Are you currently enrolled in any of these Government assisted programs below? Then you can qualify for FREE wireless service and a low-priced tablet from us.</p>
  <ul class="programs">
    <li>CalFresh, Food Stamps or Supplemental Nutrition Assistance Program <b>(SNAP)</b></li>
    <li>Medicaid/Medi-Cal</li>
    <li>Healthy Families Category A</li>
    <li>Low Income Home Energy Assistance Program <b>(LIHEAP)</b></li>
    <li>Supplemental Security Income <b>(SSI)</b></li>
    <li>Federal Public Housing Assistance or Section 8</li>
    <li>Women, Infants and Children Program <b>(WIC)</b></li>
    <li>National School Lunch Program <b>(NSL)</b></li>
    <li>Veterans &amp; Survivor Benefits</li>
    <li>Greater Avenues for Independence <b>(GAIN)</b></li>
    <li>Temporary Assistance for Needy Families <b>(TANF)</b> also called <b>CalWORKS, StanWORKS, WTW, GAIN</b></li>
    <li>California Work Opportunity and Responsibility to Kids <b>(CalWORKs)</b></li>
    <li>Stanislaus County Work Opportunity and Responsibility to Kids <b>(StanWORKs)</b></li>
    <li>Welfare-to-Work <b>(WTW)</b></li>
    <li>Tribal TANF</li>
    <li>Bureau of Indian Affairs General Assistance</li>
    <li>Head Start Income Eligible <i>(*Tribal Only)</i></li>
    <li>Food Distribution Program on Indian Reservation</li>
  </ul>
  <div class="qualify-box">
    <p class="qualify-box__text">Currently enrolled in one or more of the programs above? You could easily qualify for your FREE internet service &amp; data! Plus, a <b>NEW TABLET!</b></p>
    <div class="qualify-box__divider"></div>
    <div class="qualify-box__call">
      <svg class="qualify-box__icon" viewBox="0 0 110 110" fill="none" stroke-width="6" stroke-linecap="round"><path stroke="#1d97d8" d="M22 10l16 0 8 22-10 9c6 14 17 25 31 31l9-10 22 8v16c-40 6-82-36-76-76z"/><path stroke="#2bbfa6" d="M62 22a26 26 0 0 1 26 26M62 6a42 42 0 0 1 42 42"/></svg>
      <p class="qualify-box__line">Ask if you qualify<br><b>+800-555-0142</b></p>
    </div>
  </div>
  <p class="fine-print" style="top:1436px">Eligibility is verified through the national program database. Only one benefit per household is allowed. Supplying false information may result in loss of service. Devices are offered while supplies last. Plan details and terms can change at any time, so please check our website for current information.</p>
  <div class="footer-bar">www.brivolinkmobile.com</div>
</section>

</body>
</html>
```